TKA Electricial Contracting Services

Hi guys, after a design for my small electrical company, have logo design files to be incorporated into the layout, the basic concept is electrical contracting services for residential, commercial, industrial & data services, image is clean clear and strong,

Card format is to have a nice clean logo on front,with maybe the Residential – commercial – industrial - data, followed with licensed & insured, followed by contact details on backside of the card.

Target Market(s)

Residential, commercial, industrial sectors.

Industry/Entity Type

Electrical

Contact Information for Business Card

TKA logo,
Residential – commercial – industrial - data
REC: 61372
Email: tka@poralink.net.au
Phone: 0458 203 719

Requirements
Must have
• Clean & strong design.
Nice to have
• If possible, I would like the logo colours inverted so the text is orange and the background is black on the front of the card, then the backside of the card be the reverse colour
Should not have
• No Sparks, lightning bolts,

```html
<!DOCTYPE html>
<html lang="en">
<head>
<meta charset="utf-8">
<title>TKA Electrical Contracting Services – Business Card</title>
<link rel="stylesheet" href="https://fonts.googleapis.com/css2?family=Saira:wght@500;600;700;800&display=swap">
<style>
  :root {
    --bg: #e9e6e1;
    --black: #0b0b0b;
    --orange: #f29a1f;
    --orange-light: #f7b545;
    --orange-deep: #e5871a;
    --white: #ffffff;
    --ink: #1b1b1b;
    --rule: #dcdcdc;
  }
  * { box-sizing: border-box; margin: 0; padding: 0; }
  html, body { width: 1200px; height: 900px; overflow: hidden; }
  body {
    background: var(--bg);
    font-family: "Saira", "Arial Narrow", sans-serif;
    position: relative;
  }
  .card {
    position: absolute;
    width: 540px;
    height: 320px;
    left: 330px;
    overflow: hidden;
    box-shadow: 0 6px 18px rgba(0,0,0,.18);
  }

  /* Back: contact side */
  .card-back { top: 100px; background: var(--white); }
  .back-brand {
    position: absolute; left: 0; top: 0; bottom: 0; width: 170px;
    background: linear-gradient(90deg, var(--orange-deep), var(--orange-light));
    display: flex; flex-direction: column; justify-content: center; align-items: center;
    border-right: 6px solid var(--white);
    box-shadow: 6px 0 0 var(--orange);
  }
  .brand-name {
    font-weight: 800; letter-spacing: 2px; line-height: 1;
  }
  .back-brand .brand-name { font-size: 58px; color: var(--ink); }
  .back-brand .brand-tag { font-size: 13px; font-weight: 700; color: var(--ink); margin-top: 4px; }
  .contacts {
    position: absolute; right: 28px; top: 26px; text-align: right;
    font-size: 17px; font-weight: 500; color: var(--ink); line-height: 1.6;
  }
  .contact-line { display: flex; align-items: center; justify-content: flex-end; gap: 8px; }
  .contact-line svg { width: 14px; height: 14px; }
  .services {
    position: absolute; left: 200px; right: 24px; top: 150px;
    font-size: 15px; font-weight: 600; color: var(--ink); line-height: 1.35;
  }
  .licence-band {
    position: absolute; left: 176px; right: 0; bottom: 0; height: 46px;
    background: var(--orange);
    display: flex; align-items: center; justify-content: flex-end; padding-right: 90px;
  }
  .licence { font-size: 18px; font-weight: 700; color: var(--ink); letter-spacing: .5px; }
  .seal {
    position: absolute; right: 22px; bottom: 14px; width: 60px; height: 60px;
  }

  /* Front: logo side */
  .card-front { top: 480px; background: var(--black); }
  .front-logo {
    position: absolute; left: 0; right: 0; top: 62px; text-align: center;
    color: var(--orange);
  }
  .front-logo .brand-name { font-size: 110px; }
  .front-logo .brand-tag { font-size: 22px; font-weight: 700; margin-top: 4px; letter-spacing: .5px; }
  .sector-band {
    position: absolute; left: 0; right: 0; bottom: 0; height: 38px;
    background: var(--orange);
    display: flex; align-items: center; justify-content: center;
    font-size: 15px; font-weight: 600; color: var(--ink); letter-spacing: 2px; text-transform: uppercase;
  }
</style>
</head>
<body>

<section class="card card-back" aria-label="Business card back">
  <div class="back-brand">
    <div class="brand-name">TKA</div>
    <div class="brand-tag">Thomas Kane Electrical</div>
  </div>
  <div class="contacts">
    <div class="contact-line">0458 203 719
      <svg viewBox="0 0 24 24" aria-hidden="true"><path fill="#1b1b1b" d="M6.6 10.8a15 15 0 0 0 6.6 6.6l2.2-2.2a1 1 0 0 1 1-.25 11.4 11.4 0 0 0 3.6.57 1 1 0 0 1 1 1V20a1 1 0 0 1-1 1A17 17 0 0 1 3 4a1 1 0 0 1 1-1h3.5a1 1 0 0 1 1 1c0 1.25.2 2.45.57 3.57a1 1 0 0 1-.25 1z"/></svg>
    </div>
    <div class="contact-line">tka@poralink.net.au
      <svg viewBox="0 0 24 24" aria-hidden="true"><rect x="2" y="5" width="20" height="14" fill="none" stroke="#1b1b1b" stroke-width="2"/><path d="M2 5l10 8 10-8" fill="none" stroke="#1b1b1b" stroke-width="2"/></svg>
    </div>
  </div>
  <p class="services">New installations Additions Rewiring Repairs Maintenance 24 hours Faults and Emergency Assistance.</p>
  <div class="licence-band"><span class="licence">REC: 61372</span></div>
  <svg class="seal" viewBox="0 0 60 60" role="img" aria-label="Licensed and insured seal">
    <circle cx="30" cy="30" r="28" fill="#f7b545" stroke="#c9741a" stroke-width="3"/>
  </svg>
</section>

<section class="card card-front" aria-label="Business card front">
  <div class="front-logo">
    <div class="brand-name">TKA</div>
    <div class="brand-tag">Thomas Kane Electrical</div>
  </div>
  <div class="sector-band">Residential - Commercial - Industrial - Data</div>
</section>

</body>
</html>
```